Crestwell Renewal Business Card Design Phase 2

Professional and clean design. The design colors should flow with the logo. Two-sided card with the website on the back which is:

www.CrestwellRenewal.example.

"Specializing in Water Damage Restoration"

On the front I need the name, email, phone, and logo.

Name: Dorian Halvek
Email: Dorian@CrestwellRenewal.example
Phone: 555-318-2046 for now

I only have the Preview and Thumbnail right now but should have the source files uploaded within a day or two.

Target Market(s)

Flood victims, home owners with water damage from busted pipes etc...

Industry/Entity Type

Business

Contact Information for Business Card

Name: Dorian Halvek

Font styles to use
Serif
Sans Serif

Requirements
Must have
• Business Card Details Info

```html
<!DOCTYPE html>
<html lang="en">
<head>
<meta charset="utf-8">
<title>Crestwell Renewal – Business Card</title>
<link href="https://fonts.googleapis.com/css2?family=Tinos:wght@400;700&display=swap" rel="stylesheet">
<style>
  :root {
    --navy: #1f3763;
    --green: #4a8c3f;
    --white: #ffffff;
    --backdrop: #e9eaec;
    --rule: #5b6a88;
  }
  * { box-sizing: border-box; margin: 0; padding: 0; }
  html, body { width: 1200px; height: 780px; overflow: hidden; }
  body {
    background: var(--backdrop);
    font-family: "Tinos", "Times New Roman", serif;
    color: var(--navy);
  }
  .canvas {
    width: 1200px; height: 780px;
    display: flex; align-items: center; justify-content: center; gap: 40px;
  }
  .card {
    width: 560px; height: 320px;
    position: relative; overflow: hidden;
    box-shadow: 0 6px 18px rgba(0,0,0,.18);
  }

  /* Back side */
  .card-back { background: var(--navy); }
  .card-back .brand {
    position: absolute; left: 0; right: 0; top: 78px;
    text-align: center;
    font-weight: 700; font-size: 46px; line-height: 1;
    letter-spacing: 1px; text-transform: uppercase;
    color: var(--white);
  }
  .card-back .brand span { display: block; }
  .card-back .brand span + span { margin-top: 6px; }
  .card-back .divider {
    position: absolute; left: 0; right: 0; bottom: 58px; height: 3px;
    background: var(--white);
  }
  .card-back .web-band {
    position: absolute; left: 0; right: 0; bottom: 0; height: 58px;
    background: var(--green);
    display: flex; align-items: center; justify-content: center;
    color: var(--white); font-size: 15px; letter-spacing: .3px;
  }

  /* Front side */
  .card-front { background: var(--white); }
  .card-front .brand-block {
    position: absolute; left: 34px; top: 72px; width: 230px;
  }
  .card-front .brand {
    font-weight: 700; font-size: 38px; line-height: 1;
    text-transform: uppercase; color: var(--navy);
  }
  .card-front .brand span { display: block; }
  .card-front .brand span + span { margin-top: 4px; }
  .card-front .tagline {
    margin-top: 26px; font-size: 15px; color: var(--navy);
  }
  .card-front .vrule {
    position: absolute; left: 282px; top: 58px; width: 1px; height: 150px;
    background: var(--rule);
  }
  .card-front .contact {
    position: absolute; left: 306px; top: 60px; right: 18px;
  }
  .card-front .person {
    font-size: 20px; font-variant: small-caps; letter-spacing: .5px;
    color: var(--navy);
  }
  .card-front .details { list-style: none; margin-top: 46px; }
  .card-front .details li {
    display: flex; align-items: center; gap: 8px;
    font-size: 13.5px; line-height: 1; margin-bottom: 10px;
    white-space: nowrap;
  }
  .card-front .details svg { width: 14px; height: 14px; flex: none; }
  .card-front .green-rule {
    position: absolute; left: 0; right: 0; bottom: 52px; height: 4px;
    background: var(--green);
  }
  .card-front .navy-band {
    position: absolute; left: 0; right: 0; bottom: 0; height: 40px;
    background: var(--navy);
  }
</style>
</head>
<body>
<main class="canvas">

  <section class="card card-back" aria-label="Card back">
    <div class="brand"><span>Crestwell</span><span>Renewal</span></div>
    <div class="divider"></div>
    <div class="web-band">www.CrestwellRenewal.example</div>
  </section>

  <section class="card card-front" aria-label="Card front">
    <div class="brand-block">
      <div class="brand"><span>Crestwell</span><span>Renewal</span></div>
      <p class="tagline">Specializing in Water Damage Restoration</p>
    </div>
    <div class="vrule"></div>
    <div class="contact">
      <h1 class="person">Dorian Halvek</h1>
      <ul class="details">
        <li>
          <svg viewBox="0 0 16 16" aria-hidden="true"><path fill="#4a8c3f" d="M3.6 1.5l2.3 2.6-1.2 1.6c.9 2 2.6 3.7 4.6 4.6l1.6-1.2 2.6 2.3-1.4 2.2C6.8 14.2 1.8 9.2 1.4 2.9z"/></svg>
          555-318-2046
        </li>
        <li>
          <svg viewBox="0 0 16 16" aria-hidden="true"><rect x="1" y="3" width="14" height="10" fill="#4a8c3f"/><path d="M1.5 3.5L8 9l6.5-5.5" fill="none" stroke="#fff" stroke-width="1.3"/></svg>
          Dorian@CrestwellRenewal.example
        </li>
        <li>
          <svg viewBox="0 0 16 16" aria-hidden="true"><rect x="1.5" y="2" width="13" height="9" fill="none" stroke="#4a8c3f" stroke-width="1.6"/><path d="M6 14h4M8 11v3" stroke="#4a8c3f" stroke-width="1.6"/></svg>
          www.CrestwellRenewal.example
        </li>
      </ul>
    </div>
    <div class="green-rule"></div>
    <div class="navy-band"></div>
  </section>

</main>
</body>
</html>
```